Solids Control Presentation Template Design

I'm putting together a technical 5-day course about solids control and waste management. I'm looking for an updated art and a easy on the eyes format.

```html
<!DOCTYPE html>
<html lang="en">
<head>
<meta charset="utf-8">
<title>Solids Control Presentation Template</title>
<link href="https://fonts.googleapis.com/css2?family=Poppins:wght@400;500;600;700;800&display=swap" rel="stylesheet">
<style>
:root{
  --red:#9b2a2f;
  --red-dark:#7d1f24;
  --ink:#231f20;
  --grey:#e4e4e4;
  --grey-mid:#d3d3d3;
  --text:#555;
  --white:#fff;
  --stage:#000;
}
*{box-sizing:border-box;margin:0;padding:0}
html,body{width:1200px;height:690px;overflow:hidden;background:var(--stage);font-family:'Poppins',sans-serif}
.deck{position:relative;width:1200px;height:690px}
.slide{position:absolute;width:391px;height:220px;background:var(--white);overflow:hidden}
.abs{position:absolute}
.photo{position:absolute}
.tiny{font-size:4.3px;line-height:5.6px;color:var(--text)}
.brand-mini{position:absolute;right:8px;top:5px;text-align:right}
.brand-mini .name{font-size:10px;font-weight:800;color:var(--ink);letter-spacing:.5px;line-height:10px}
.brand-mini .tag{font-size:3.3px;color:var(--ink);letter-spacing:.3px}
.footer{position:absolute;left:0;bottom:0;width:100%;height:13px}
.footer .page{position:absolute;right:12px;bottom:3px;font-size:5px;font-weight:700;color:var(--white)}
.heading{font-weight:700;color:var(--ink);text-transform:uppercase}
.heading em{font-style:normal;color:var(--red)}
.badge{display:flex;align-items:center;justify-content:center;color:var(--white);font-weight:700;font-size:5.5px;background:var(--red)}
.hex-badge{width:15px;height:16px;clip-path:polygon(50% 0,100% 25%,100% 75%,50% 100%,0 75%,0 25%)}
.item-title{font-size:5.4px;font-weight:700;color:var(--ink)}
</style>
</head>
<body>
<div class="deck">

<!-- Cover -->
<section class="slide cover" style="left:8px;top:10px;background:var(--red)">
  <div class="photo" role="img" aria-label="Oil field pump jacks silhouetted against a red sunset sky" style="left:0;top:0;width:230px;height:220px;background:linear-gradient(180deg,#c9a1a3 0%,#a4565b 45%,#5b1a1e 100%);clip-path:polygon(0 0,190px 0,230px 220px,0 220px)"></div>
  <svg class="abs" style="left:0;top:0" width="391" height="220" aria-hidden="true">
    <polygon points="160,0 195,0 235,220 200,220" fill="var(--red-dark)" opacity=".9"/>
    <polygon points="0,150 40,220 0,220" fill="var(--red)"/>
    <polygon points="195,140 215,220 232,220" fill="var(--ink)"/>
  </svg>
  <div class="abs" style="right:10px;top:66px;text-align:right;color:var(--white)">
    <div style="font-size:18.5px;font-weight:700;line-height:24px">RESULTS DRIVEN<br>SOLIDS CONTROL</div>
    <div style="font-size:7px;font-weight:700;margin-top:6px">RUNNING THE BACKYARD BY THE NUMBERS</div>
  </div>
  <div class="abs" style="right:10px;top:153px;text-align:center;color:var(--white)">
    <div style="font-size:21px;font-weight:800;letter-spacing:1px;line-height:22px">RIDGEPOINT</div>
    <div style="font-size:8.5px;letter-spacing:1px">Precision Well Solutions</div>
    <div style="font-size:4.6px;letter-spacing:.8px;margin-top:1px">ENGINEERING • CONSULTING • TRAINING • EQUIPMENT</div>
  </div>
</section>

<!-- Engineering services -->
<section class="slide services" style="left:405px;top:10px">
  <div class="brand-mini"><div class="name">RIDGEPOINT</div><div class="tag">ENGINEERING • CONSULTING • TRAINING</div></div>
  <div class="heading abs" style="left:0;width:100%;top:21px;text-align:center;font-size:13px">Our <em>Engineering</em> Services</div>
  <div class="abs" style="left:59px;top:52px;display:grid;grid-template-columns:repeat(3,88px);gap:6px">
    <div class="service-card" style="height:67px;border:1px solid #e6e6e6;border-radius:10px;text-align:center;padding:6px 6px 0"><div class="badge" style="width:15px;height:15px;border-radius:4px;margin:0 auto 5px">01</div><div class="item-title">Services - 01</div><p class="tiny">Lorem ipsum dolor sit amet, consectetur adipiscing elit, sed do eiusmod tempor incididunt ut labor aliqua.</p></div>
    <div class="service-card" style="height:67px;border:1px solid #e6e6e6;border-radius:10px;text-align:center;padding:6px 6px 0"><div class="badge" style="width:15px;height:15px;border-radius:4px;margin:0 auto 5px">02</div><div class="item-title">Services - 02</div><p class="tiny">Lorem ipsum dolor sit amet, consectetur adipiscing elit, sed do eiusmod tempor incididunt ut labor aliqua.</p></div>
    <div class="service-card" style="height:67px;border:1px solid #e6e6e6;border-radius:10px;text-align:center;padding:6px 6px 0"><div class="badge" style="width:15px;height:15px;border-radius:4px;margin:0 auto 5px">03</div><div class="item-title">Services - 03</div><p class="tiny">Lorem ipsum dolor sit amet, consectetur adipiscing elit, sed do eiusmod tempor incididunt ut labor aliqua.</p></div>
    <div class="service-card" style="height:67px;border:1px solid #e6e6e6;border-radius:10px;text-align:center;padding:6px 6px 0"><div class="badge" style="width:15px;height:15px;border-radius:4px;margin:0 auto 5px">04</div><div class="item-title">Services - 04</div><p class="tiny">Lorem ipsum dolor sit amet, consectetur adipiscing elit, sed do eiusmod tempor incididunt ut labor aliqua.</p></div>
    <div class="service-card" style="height:67px;border:1px solid #e6e6e6;border-radius:10px;text-align:center;padding:6px 6px 0"><div class="badge" style="width:15px;height:15px;border-radius:4px;margin:0 auto 5px">05</div><div class="item-title">Services - 05</div><p class="tiny">Lorem ipsum dolor sit amet, consectetur adipiscing elit, sed do eiusmod tempor incididunt ut labor aliqua.</p></div>
    <div class="service-card" style="height:67px;border:1px solid #e6e6e6;border-radius:10px;text-align:center;padding:6px 6px 0"><div class="badge" style="width:15px;height:15px;border-radius:4px;margin:0 auto 5px">06</div><div class="item-title">Services - 06</div><p class="tiny">Lorem ipsum dolor sit amet, consectetur adipiscing elit, sed do eiusmod tempor incididunt ut labor aliqua.</p></div>
  </div>
  <svg class="footer" width="391" height="13" aria-hidden="true"><rect width="391" height="13" fill="var(--red)" y="6"/><polygon points="318,0 391,0 391,13 330,13" fill="var(--ink)"/><polygon points="308,0 316,0 328,13 320,13" fill="var(--white)"/></svg>
  <div class="footer"><span class="page">PAGE : 01</span></div>
</section>

<!-- Course agenda table -->
<section class="slide agenda" style="left:802px;top:10px">
  <div class="brand-mini"><div class="name">RIDGEPOINT</div><div class="tag">ENGINEERING • CONSULTING • TRAINING</div></div>
  <div class="heading abs" style="left:0;width:100%;top:26px;text-align:center;font-size:9px">Our Course Agenda Table</div>
  <table class="agenda-table abs" style="left:40px;top:53px;width:311px;border-collapse:collapse;font-size:3.8px;color:#444">
    <thead><tr style="background:var(--red);color:var(--white);height:15px;font-weight:700;text-align:left"><th style="padding-left:6px;border-right:1px solid #fff">Table Title here</th><th style="padding-left:6px;border-right:1px solid #fff">Table Title here</th><th style="padding-left:6px;border-right:1px solid #fff">Table Title here</th><th style="padding-left:6px">Table Title here</th></tr></thead>
    <tbody style="background:var(--grey)">
      <tr style="height:10px"><td style="padding-left:6px">Paragraph Text Here</td><td style="padding-left:6px">Paragraph Text Here</td><td style="padding-left:6px">Paragraph Text Here</td><td style="padding-left:6px">Paragraph Text Here</td></tr>
      <tr style="height:10px"><td style="padding-left:6px">Paragraph Text Here</td><td style="padding-left:6px">Paragraph Text Here</td><td style="padding-left:6px">Paragraph Text Here</td><td style="padding-left:6px">Paragraph Text Here</td></tr>
      <tr style="height:10px"><td style="padding-left:6px">Paragraph Text Here</td><td style="padding-left:6px">Paragraph Text Here</td><td style="padding-left:6px">Paragraph Text Here</td><td style="padding-left:6px">Paragraph Text Here</td></tr>
      <tr style="height:10px"><td style="padding-left:6px">Paragraph Text Here</td><td style="padding-left:6px">Paragraph Text Here</td><td style="padding-left:6px">Paragraph Text Here</td><td style="padding-left:6px">Paragraph Text Here</td></tr>
      <tr style="height:10px"><td style="padding-left:6px">Paragraph Text Here</td><td style="padding-left:6px">Paragraph Text Here</td><td style="padding-left:6px">Paragraph Text Here</td><td style="padding-left:6px">Paragraph Text Here</td></tr>
      <tr style="height:10px"><td style="padding-left:6px">Paragraph Text Here</td><td style="padding-left:6px">Paragraph Text Here</td><td style="padding-left:6px">Paragraph Text Here</td><td style="padding-left:6px">Paragraph Text Here</td></tr>
      <tr style="height:10px"><td style="padding-left:6px">Paragraph Text Here</td><td style="padding-left:6px">Paragraph Text Here</td><td style="padding-left:6px">Paragraph Text Here</td><td style="padding-left:6px">Paragraph Text Here</td></tr>
      <tr style="height:10px"><td style="padding-left:6px">Paragraph Text Here</td><td style="padding-left:6px">Paragraph Text Here</td><td style="padding-left:6px">Paragraph Text Here</td><td style="padding-left:6px">Paragraph Text Here</td></tr>
      <tr style="height:10px"><td style="padding-left:6px">Paragraph Text Here</td><td style="padding-left:6px">Paragraph Text Here</td><td style="padding-left:6px">Paragraph Text Here</td><td style="padding-left:6px">Paragraph Text Here</td></tr>
      <tr style="height:10px"><td style="padding-left:6px">Paragraph Text Here</td><td style="padding-left:6px">Paragraph Text Here</td><td style="padding-left:6px">Paragraph Text Here</td><td style="padding-left:6px">Paragraph Text Here</td></tr>
      <tr style="height:10px"><td style="padding-left:6px">Paragraph Text Here</td><td style="padding-left:6px">Paragraph Text Here</td><td style="padding-left:6px">Paragraph Text Here</td><td style="padding-left:6px">Paragraph Text Here</td></tr>
      <tr style="height:10px"><td style="padding-left:6px">Paragraph Text Here</td><td style="padding-left:6px">Paragraph Text Here</td><td style="padding-left:6px">Paragraph Text Here</td><td style="padding-left:6px">Paragraph Text Here</td></tr>
      <tr style="height:10px"><td style="padding-left:6px">Paragraph Text Here</td><td style="padding-left:6px">Paragraph Text Here</td><td style="padding-left:6px">Paragraph Text Here</td><td style="padding-left:6px">Paragraph Text Here</td></tr>
    </tbody>
  </table>
  <svg class="footer" width="391" height="13" aria-hidden="true"><rect width="391" height="13" fill="var(--red)" y="6"/><polygon points="325,0 391,0 391,13 337,13" fill="var(--ink)"/><polygon points="315,0 323,0 335,13 327,13" fill="var(--white)"/></svg>
  <div class="footer"><span class="page">PAGE : 01</span></div>
</section>

<!-- Training courses -->
<section class="slide training" style="left:8px;top:236px">
  <div class="photo" role="img" aria-label="Hands with a pen working beside a laptop on a desk" style="left:0;top:0;width:250px;height:220px;background:linear-gradient(135deg,#8f9a97 0%,#c7cecb 55%,#9aa3a0 100%);clip-path:polygon(0 0,235px 0,160px 220px,0 220px)"></div>
  <svg class="abs" style="left:0;top:0" width="391" height="220" aria-hidden="true">
    <polygon points="235,0 250,0 175,220 160,220" fill="var(--white)"/>
    <polygon points="391,90 391,220 365,220" fill="var(--red)"/>
  </svg>
  <div class="brand-mini"><div class="name">RIDGEPOINT</div><div class="tag">ENGINEERING • CONSULTING • TRAINING</div></div>
  <div class="abs" style="left:216px;top:54px;width:150px">
    <div class="heading" style="font-size:9.5px;color:var(--red)">Our Training Courses</div>
    <p class="tiny" style="margin-top:2px">Lorem ipsum dolor sit amet, consectetur adipi scing elit, sed do eiusmod tempor incididunt ut labore dolore magna aliqua.</p>
  </div>
  <div class="abs course-list" style="left:218px;top:88px;width:150px">
    <div style="display:flex;gap:7px;margin-bottom:9px"><div class="badge hex-badge" style="flex:none"></div><div><div class="item-title">Solids Control for Drilling Engineers</div><p class="tiny">Lorem ipsum dolor sit amet, consectetur adipiscing elit, sed do eiusmod tempor incididunt ut labor aliqua.</p></div></div>
    <div style="display:flex;gap:7px;margin-bottom:9px"><div class="badge hex-badge" style="flex:none"></div><div><div class="item-title">Drilling Waste Handling and Treatment</div><p class="tiny">Lorem ipsum dolor sit amet, consectetur adipiscing elit, sed do eiusmod tempor incididunt ut labor aliqua.</p></div></div>
    <div style="display:flex;gap:7px;margin-bottom:9px"><div class="badge hex-badge" style="flex:none"></div><div><div class="item-title">Water Treatment</div><p class="tiny">Lorem ipsum dolor sit amet, consectetur adipiscing elit, sed do eiusmod tempor incididunt ut labor aliqua.</p></div></div>
    <div style="display:flex;gap:7px"><div class="badge hex-badge" style="flex:none"></div><div><div class="item-title">Solids Control for the Sales Team</div><p class="tiny">Lorem ipsum dolor sit amet, consectetur adipiscing elit, sed do eiusmod tempor incididunt ut labor aliqua.</p></div></div>
  </div>
</section>

<!-- Process flow -->
<section class="slide process" style="left:405px;top:236px">
  <div class="photo" role="img" aria-label="Two workers in hard hats shaking hands, silhouetted against the sky" style="left:0;top:0;width:146px;height:220px;background:linear-gradient(180deg,#5d6e84 0%,#a9b4bf 60%,#3a3f47 100%)"></div>
  <div class="brand-mini"><div class="name">RIDGEPOINT</div><div class="tag">ENGINEERING • CONSULTING • TRAINING</div></div>
  <svg class="abs" style="left:0;top:0" width="391" height="220" aria-hidden="true">
    <circle cx="153" cy="110" r="38" fill="var(--white)"/>
    <path d="M153 72 A38 38 0 0 1 153 148" fill="none" stroke="var(--red)" stroke-width="5"/>
    <circle cx="153" cy="110" r="22" fill="var(--white)" stroke="#ddd" stroke-width="1"/>
    <circle cx="153" cy="107" r="6" fill="none" stroke="var(--red)" stroke-width="1.4"/>
    <rect x="150" y="114" width="6" height="4" fill="var(--red)"/>
    <g stroke="#999" stroke-width=".6" fill="none">
      <path d="M191 110 H205"/><path d="M172 80 V59 H196"/><path d="M172 140 V162 H196"/>
    </g>
    <polygon points="196,40 345,40 338,59 345,78 196,78 203,59" fill="var(--red)"/>
    <polygon points="212,91 368,91 361,110 368,129 212,129 219,110" fill="var(--ink)"/>
    <polygon points="196,143 345,143 338,162 345,181 196,181 203,162" fill="var(--red)"/>
    <polygon points="330,205 391,205 391,220 318,220" fill="var(--ink)"/>
  </svg>
  <div class="abs" style="left:210px;top:46px;width:125px;color:var(--white)"><div class="item-title" style="color:var(--white)">Business Market Research</div><p class="tiny" style="color:#eee">Lorem ipsum dolor sit amet, consectetur adipiscing elit, sed do eiusmod tempor incididunt ut labor aliqua.</p></div>
  <div class="abs" style="left:232px;top:97px;width:125px"><div class="item-title" style="color:var(--white)">Finding Creative Solutions</div><p class="tiny" style="color:#eee">Lorem ipsum dolor sit amet, consectetur adipiscing elit, sed do eiusmod tempor incididunt ut labor aliqua.</p></div>
  <div class="abs" style="left:210px;top:149px;width:125px"><div class="item-title" style="color:var(--white)">Solving Problem With Confident</div><p class="tiny" style="color:#eee">Lorem ipsum dolor sit amet, consectetur adipiscing elit, sed do eiusmod tempor incididunt ut labor aliqua.</p></div>
  <div class="footer"><span class="page">PAGE : 01</span></div>
</section>

<!-- Thank you -->
<section class="slide thanks" style="left:802px;top:236px;background:var(--red)">
  <div class="photo" role="img" aria-label="Modern glass office building on a lawn at dusk" style="left:0;top:0;width:391px;height:220px;background:linear-gradient(180deg,#4f6fa5 0%,#b7aac4 45%,#d8b6b5 62%,#5d7348 80%,#3f5530 100%);clip-path:polygon(280px 0,391px 0,391px 220px,215px 220px)"></div>
  <svg class="abs" style="left:0;top:0" width="391" height="220" aria-hidden="true">
    <polygon points="270,0 282,0 217,220 205,220" fill="var(--ink)"/>
    <polygon points="0,55 165,55 150,85 0,85" fill="var(--ink)"/>
  </svg>
  <div class="abs" style="left:24px;top:60px;font-size:14px;font-weight:700;color:var(--white)">THANK YOU</div>
  <div class="abs" style="left:24px;top:96px;color:var(--white);text-align:center">
    <div style="font-size:16px;font-weight:800;letter-spacing:1px;line-height:17px">RIDGEPOINT</div>
    <div style="font-size:6.5px;letter-spacing:.8px">Precision Well Solutions</div>
    <div style="font-size:3.6px;letter-spacing:.5px">ENGINEERING • CONSULTING • TRAINING • EQUIPMENT</div>
  </div>
  <address class="abs" style="left:24px;top:132px;font-style:normal;font-size:6.2px;line-height:12.5px;color:var(--white)">
    4410 LINDEN PARK DR<br>HOUSTON, TEXAS 77042<br>PHONE: 281-555-0147<br>EMAIL: INFO@RIDGEPOINT-ENG.COM
  </address>
</section>

<!-- Clients -->
<section class="slide clients" style="left:8px;top:466px">
  <div class="brand-mini"><div class="name">RIDGEPOINT</div><div class="tag">ENGINEERING • CONSULTING • TRAINING</div></div>
  <div class="abs" style="left:25px;top:30px;width:185px">
    <div class="heading" style="font-size:13px;color:var(--red)">Our Clients</div>
    <p class="tiny" style="font-size:5px;line-height:6.5px;margin-top:3px">Lorem ipsum dolor sit amet, consectetur adipi scing elit, sed do eiusmod tempor incididunt ut labore dolore magna aliqua.</p>
  </div>
  <div class="abs" style="left:25px;top:80px;width:150px">
    <div style="display:flex;gap:7px;margin-bottom:8px"><div class="badge hex-badge" style="flex:none">01</div><div><div class="item-title">Experience</div><p class="tiny">Dolor sit amet, consectetur adipiscing elit, sed do eiusmod tempor incididunt ut labor aliqua.</p></div></div>
    <div style="display:flex;gap:7px;margin-bottom:8px"><div class="badge hex-badge" style="flex:none">02</div><div><div class="item-title">Excellence</div><p class="tiny">Ipsum dolor sit amet, consectetur adipiscing elit, sed do eiusmod tempor incididunt ut labor aliqua.</p></div></div>
    <div style="display:flex;gap:7px"><div class="badge hex-badge" style="flex:none">03</div><div><div class="item-title">Effective</div><p class="tiny">Dolor sit amet, consectetur adipiscing elit, sed do eiusmod tempor incididunt ut labor aliqua.</p></div></div>
  </div>
  <svg class="abs client-hexes" style="left:185px;top:20px" width="175" height="180" aria-hidden="true">
    <g fill="var(--white)" stroke="#ccc" stroke-width=".8">
      <polygon points="60,2 88,18 88,50 60,66 32,50 32,18"/>
      <polygon points="120,2 148,18 148,50 120,66 92,50 92,18"/>
      <polygon points="30,56 58,72 58,104 30,120 2,104 2,72"/>
      <polygon points="90,56 118,72 118,104 90,120 62,104 62,72"/>
      <polygon points="150,56 178,72 178,104 150,120 122,104 122,72"/>
      <polygon points="60,110 88,126 88,158 60,174 32,158 32,126"/>
      <polygon points="120,110 148,126 148,158 120,174 92,158 92,126"/>
    </g>
    <g font-family="Poppins, sans-serif" font-size="6.2" font-weight="600" fill="var(--ink)" text-anchor="middle">
      <text x="60" y="36">Northfield Oil</text>
      <text x="120" y="36">Halden Energy</text>
      <text x="30" y="90">Corvan</text>
      <text x="90" y="90">Westmark</text>
      <text x="148" y="90">Solara</text>
      <text x="60" y="144">Brightmoor</text>
      <text x="120" y="144">Kestrel Gas</text>
    </g>
  </svg>
  <svg class="footer" width="391" height="13" aria-hidden="true"><rect width="391" height="13" fill="var(--red)" y="2"/><polygon points="330,0 391,0 391,13 342,13" fill="var(--white)"/><polygon points="322,0 328,0 340,13 334,13" fill="var(--ink)"/></svg>
  <div class="footer"><span style="position:absolute;left:6px;bottom:2px;font-size:5px;font-weight:700;color:var(--white)">COPYRIGHT TEXT HERE</span><span class="page" style="color:var(--ink);font-weight:500">Page : 01</span></div>
</section>

<!-- Tracking progress -->
<section class="slide progress" style="left:405px;top:466px">
  <div class="photo" role="img" aria-label="Drilling mud and cuttings on a shaker screen" style="left:0;top:0;width:80px;height:103px;background:linear-gradient(160deg,#8a8172,#c7bfae 55%,#6d6658)"></div>
  <div class="photo" role="img" aria-label="Technician in protective gloves handling equipment" style="left:84px;top:10px;width:80px;height:103px;background:linear-gradient(160deg,#b8bcc0,#e3e3e1 50%,#6f8a5a)"></div>
  <div class="photo" role="img" aria-label="Muddy drilling site with water runoff" style="left:0;top:107px;width:80px;height:113px;background:linear-gradient(160deg,#7d6b55,#a49683 50%,#4e5b66)"></div>
  <div class="photo" role="img" aria-label="Modern office building under a blue sky" style="left:84px;top:117px;width:80px;height:90px;background:linear-gradient(180deg,#5c7fb3,#b4c1d6 60%,#627a4a)"></div>
  <div class="brand-mini"><div class="name">RIDGEPOINT</div><div class="tag">ENGINEERING • CONSULTING • TRAINING</div></div>
  <div class="abs" style="left:195px;top:32px;width:180px">
    <div class="heading" style="font-size:10px">How We Track <em>Our Progress</em></div>
    <p class="tiny" style="margin-top:2px">Lorem ipsum dolor sit amet, consectetur adipi scing elit, sed do eiusmod tempor incididunt ut labore dolore magna aliqua.</p>
  </div>
  <div class="abs" style="left:195px;top:70px;width:170px">
    <div style="display:flex;gap:7px;margin-bottom:9px"><div class="badge hex-badge" style="flex:none">01</div><div><div class="item-title">Break out large tasks into smaller pieces</div><p class="tiny">Lorem ipsum dolor sit amet, consectetur adipiscing elit, sed do eiusmod tempor incididunt ut labor aliqua.</p></div></div>
    <div style="display:flex;gap:7px;margin-bottom:9px"><div class="badge hex-badge" style="flex:none">02</div><div><div class="item-title">Set daily quotas and start every day at zero</div><p class="tiny">Lorem ipsum dolor sit amet, consectetur adipiscing elit, sed do eiusmod tempor incididunt ut labor aliqua.</p></div></div>
    <div style="display:flex;gap:7px;margin-bottom:9px"><div class="badge hex-badge" style="flex:none">03</div><div><div class="item-title">Using app to track progress on specific goals</div><p class="tiny">Lorem ipsum dolor sit amet, consectetur adipiscing elit, sed do eiusmod tempor incididunt ut labor aliqua.</p></div></div>
    <div style="display:flex;gap:7px"><div class="badge hex-badge" style="flex:none">04</div><div><div class="item-title">Track our metrics on a calendar</div><p class="tiny">Lorem ipsum dolor sit amet, consectetur adipiscing elit, sed do eiusmod tempor incididunt ut labor aliqua.</p></div></div>
  </div>
  <svg class="footer" width="391" height="13" aria-hidden="true"><rect x="165" width="226" height="13" fill="var(--red)" y="5"/><polygon points="325,0 391,0 391,13 337,13" fill="var(--ink)"/><polygon points="315,0 323,0 335,13 327,13" fill="var(--white)"/></svg>
  <div class="footer"><span class="page">PAGE : 01</span></div>
</section>

</div>
</body>
</html>
```